World travel poster - I want to remember where I've been!

I would like a poster for me to print and keep in my home as a record of my world travels. It must look like a mechanical sign in an airport (see picture for example) However I am flexible with exact layout, if you'd like to add images used to enhance poster etc. I have also uploaded some pictures from my travels if you would like to use some or all of them. They are named according to location.

Poster must include:
USA 2003
Malaysia 2006
Thailand 2007
Italy 2009
India, Vietnam, Hong Kong 2010
Bali 2011
Malaysia 2012
Singapore 2012
Vietnam, Cambodia, Laos 2013
Europe 2015

and the quote:

"The world is a book and those who do not travel read only one page."
― Corwin of Veldmarsh
Updates

Hi there. I have uploaded some photos of my travels to possibly use in my poster. They are named according to location. I haven't decided if I prefer the originial layout or with images, so please post both for me to consider. Thanks so much for your time to consider my project.

Target Market(s)

Something to catch the eye of visitors and remind me of my adventures.
A classic piece that is a conversation starter.

Industry/Entity Type

Airport

Font styles to use
Other font styles liked:
• Airport mechanical font

Requirements
Must have
• Some lettering like a mechanical airport board (see image attached for example).
Dimensions that are easy to print - either A3, or a long/narrow poster.
Nice to have
• A splash of colour or an image, maybe the words 'arrivals' or 'departures'

Use of some of my pictures if it doesn't look too busy.
Should not have
• Anything too over the top.

```html
<!DOCTYPE html>
<html lang="en">
<head>
<meta charset="utf-8">
<title>Departures – Travel Record</title>
<link href="https://fonts.googleapis.com/css2?family=Montserrat:wght@300;600;700&family=Roboto+Condensed:wght@700&display=swap" rel="stylesheet">
<style>
  :root{
    --board:#2a2a2b;
    --board-deep:#232324;
    --flap-top:#3b3b3d;
    --flap-bottom:#2e2e30;
    --flap-edge:#18181a;
    --flap-text:#f4f4f2;
    --year-text:#f1e3a8;
    --accent:#f7d417;
    --quote:#e9e9e9;
    --photo-frame:#fbfbfb;
  }
  *{box-sizing:border-box;margin:0;padding:0}
  html,body{width:837px;height:1200px;overflow:hidden;background:var(--board)}
  .poster{position:relative;width:837px;height:1200px;
    background:radial-gradient(ellipse at 40% 35%,#323234 0%,var(--board) 55%,var(--board-deep) 100%);
    font-family:"Montserrat",sans-serif;}

  .header{position:absolute;left:32px;top:30px;display:flex;align-items:center;gap:22px}
  .header__icon{width:70px;height:34px}
  .header__title{font-weight:600;font-size:44px;letter-spacing:5px;color:var(--accent)}

  .board-row{position:absolute;left:32px;display:flex;height:56px}
  .flap{position:relative;width:41px;height:56px;margin-right:4px;border-radius:3px;
    background:linear-gradient(to bottom,var(--flap-top) 0%,var(--flap-top) 49%,var(--flap-bottom) 51%,var(--flap-bottom) 100%);
    box-shadow:0 2px 3px rgba(0,0,0,.55), inset 0 0 0 1px rgba(255,255,255,.05);
    font-family:"Roboto Condensed",sans-serif;font-weight:700;font-size:40px;line-height:56px;
    text-align:center;color:var(--flap-text)}
  .flap::after{content:"";position:absolute;left:0;right:0;top:27px;height:2px;background:var(--flap-edge)}
  .flap--year{color:var(--year-text)}
  .flap--amp{color:var(--year-text)}

  .flag{position:absolute;width:84px;height:50px;box-shadow:0 2px 4px rgba(0,0,0,.5)}

  .snapshot{position:absolute;background:var(--photo-frame);padding:6px;
    box-shadow:0 3px 8px rgba(0,0,0,.55)}
  .snapshot__fill{width:100%;height:100%}

  .quote{position:absolute;left:34px;top:948px;width:780px;color:var(--quote);
    font-weight:300;font-size:41px;line-height:57px}
  .quote__highlight{font-weight:700;color:var(--accent)}
  .quote__book{width:66px;height:34px;vertical-align:-4px;margin-left:12px}
  .quote__author{display:block;font-size:19px;line-height:30px;margin-top:4px;font-weight:300}
</style>
</head>
<body>
<main class="poster">

  <header class="header">
    <svg class="header__icon" viewBox="0 0 70 34" aria-hidden="true">
      <path d="M2 17 Q2 13 8 13 L26 13 L14 1 L22 1 L42 13 L60 13 Q68 13 68 17 Q68 21 60 21 L42 21 L22 33 L14 33 L26 21 L8 21 Q2 21 2 17Z" fill="#f7d417"/>
    </svg>
    <h1 class="header__title">DEPARTURES</h1>
  </header>

  <!-- row 1 -->
  <div class="board-row" style="top:121px"><span class="flap">U</span><span class="flap">S</span><span class="flap">A</span><span class="flap">–</span><span class="flap flap--year">2</span><span class="flap flap--year">0</span><span class="flap flap--year">0</span><span class="flap flap--year">3</span></div>
  <svg class="flag" style="left:400px;top:124px" viewBox="0 0 30 18" aria-label="USA flag"><rect width="30" height="18" fill="#fff"/><g fill="#c8102e"><rect y="0" width="30" height="1.4"/><rect y="2.8" width="30" height="1.4"/><rect y="5.5" width="30" height="1.4"/><rect y="8.3" width="30" height="1.4"/><rect y="11.1" width="30" height="1.4"/><rect y="13.8" width="30" height="1.4"/><rect y="16.6" width="30" height="1.4"/></g><rect width="12" height="9.7" fill="#1f3a8a"/></svg>

  <!-- row 2 -->
  <div class="board-row" style="top:191px"><span class="flap">M</span><span class="flap">A</span><span class="flap">L</span><span class="flap">A</span><span class="flap">Y</span><span class="flap">S</span><span class="flap">I</span><span class="flap">A</span><span class="flap">–</span><span class="flap flap--year">2</span><span class="flap flap--year">0</span><span class="flap flap--year">0</span><span class="flap flap--year">6</span></div>
  <svg class="flag" style="left:625px;top:194px" viewBox="0 0 30 18" aria-label="Malaysia flag"><rect width="30" height="18" fill="#fff"/><g fill="#cc0001"><rect y="0" width="30" height="1.3"/><rect y="2.6" width="30" height="1.3"/><rect y="5.1" width="30" height="1.3"/><rect y="7.7" width="30" height="1.3"/><rect y="10.3" width="30" height="1.3"/><rect y="12.9" width="30" height="1.3"/><rect y="15.4" width="30" height="1.3"/></g><rect width="15" height="10.3" fill="#010066"/><circle cx="6" cy="5.1" r="3" fill="#fc0"/><circle cx="7.2" cy="5.1" r="2.5" fill="#010066"/><circle cx="11" cy="5.1" r="1.6" fill="#fc0"/></svg>
  <figure class="snapshot" style="left:716px;top:170px;width:114px;height:88px;transform:rotate(3deg)"><div class="snapshot__fill" role="img" aria-label="Travel photo: friends together in Malaysia" style="background:linear-gradient(135deg,#b7a89a,#6d5b55 60%,#3c3434)"></div></figure>

  <!-- row 3 -->
  <div class="board-row" style="top:261px"><span class="flap">T</span><span class="flap">H</span><span class="flap">A</span><span class="flap">I</span><span class="flap">L</span><span class="flap">A</span><span class="flap">N</span><span class="flap">D</span><span class="flap">–</span><span class="flap flap--year">2</span><span class="flap flap--year">0</span><span class="flap flap--year">0</span><span class="flap flap--year">7</span></div>
  <svg class="flag" style="left:625px;top:264px" viewBox="0 0 30 18" aria-label="Thailand flag"><rect width="30" height="18" fill="#a51931"/><rect y="3" width="30" height="12" fill="#f4f5f8"/><rect y="6" width="30" height="6" fill="#2d2a4a"/></svg>

  <!-- row 4 -->
  <div class="board-row" style="top:331px"><span class="flap">I</span><span class="flap">T</span><span class="flap">A</span><span class="flap">L</span><span class="flap">Y</span><span class="flap">–</span><span class="flap flap--year">2</span><span class="flap flap--year">0</span><span class="flap flap--year">0</span><span class="flap flap--year">9</span></div>
  <svg class="flag" style="left:490px;top:334px" viewBox="0 0 30 18" aria-label="Italy flag"><rect width="10" height="18" fill="#009246"/><rect x="10" width="10" height="18" fill="#fff"/><rect x="20" width="10" height="18" fill="#ce2b37"/></svg>
  <figure class="snapshot" style="left:562px;top:305px;width:112px;height:96px;transform:rotate(-4deg)"><div class="snapshot__fill" role="img" aria-label="Travel photo: couple portrait in Italy" style="background:linear-gradient(135deg,#8c9a7a,#6f6450 55%,#3e3a33)"></div></figure>

  <!-- row 5 -->
  <div class="board-row" style="top:401px"><span class="flap">I</span><span class="flap">N</span><span class="flap">D</span><span class="flap">I</span><span class="flap">A</span><span class="flap">,</span><span class="flap">V</span><span class="flap">I</span><span class="flap">E</span><span class="flap">T</span><span class="flap">N</span><span class="flap">A</span><span class="flap">M</span></div>
  <svg class="flag" style="left:625px;top:404px" viewBox="0 0 30 18" aria-label="India flag"><rect width="30" height="6" fill="#ff9933"/><rect y="6" width="30" height="6" fill="#fff"/><rect y="12" width="30" height="6" fill="#138808"/><circle cx="15" cy="9" r="2.2" fill="none" stroke="#000080" stroke-width=".6"/></svg>
  <svg class="flag" style="left:724px;top:404px" viewBox="0 0 30 18" aria-label="Vietnam flag"><rect width="30" height="18" fill="#da251d"/><polygon points="15,3.5 16.4,7.6 20.7,7.6 17.2,10.1 18.5,14.2 15,11.7 11.5,14.2 12.8,10.1 9.3,7.6 13.6,7.6" fill="#ff0"/></svg>

  <!-- row 6 -->
  <div class="board-row" style="top:471px"><span class="flap flap--amp">&amp;</span><span class="flap">H</span><span class="flap">O</span><span class="flap">N</span><span class="flap">G</span><span class="flap">K</span><span class="flap">O</span><span class="flap">N</span><span class="flap">G</span><span class="flap flap--year">2</span><span class="flap flap--year">0</span><span class="flap flap--year">1</span><span class="flap flap--year">0</span></div>
  <svg class="flag" style="left:625px;top:474px" viewBox="0 0 30 18" aria-label="Hong Kong flag"><rect width="30" height="18" fill="#de2910"/><circle cx="15" cy="9" r="4" fill="#fff"/><circle cx="15" cy="9" r="1.2" fill="#de2910"/></svg>
  <figure class="snapshot" style="left:716px;top:440px;width:114px;height:94px;transform:rotate(-3deg)"><div class="snapshot__fill" role="img" aria-label="Travel photo: festive dinner in Hong Kong" style="background:linear-gradient(135deg,#d7a35a,#b24a33 55%,#5a2a22)"></div></figure>

  <!-- row 7 -->
  <div class="board-row" style="top:541px"><span class="flap">B</span><span class="flap">A</span><span class="flap">L</span><span class="flap">I</span><span class="flap">–</span><span class="flap flap--year">2</span><span class="flap flap--year">0</span><span class="flap flap--year">1</span><span class="flap flap--year">1</span></div>
  <svg class="flag" style="left:445px;top:544px" viewBox="0 0 30 18" role="img" aria-label="Bali provincial flag with emblem"><rect width="30" height="18" fill="#f29a1f"/><rect x="11" y="4" width="8" height="10" rx="2" fill="#3f6eb0"/></svg>
  <figure class="snapshot" style="left:530px;top:518px;width:104px;height:90px;transform:rotate(5deg)"><div class="snapshot__fill" role="img" aria-label="Travel photo: cooking class in Bali" style="background:linear-gradient(135deg,#d9d2c4,#9a8c78 60%,#5b5045)"></div></figure>

  <!-- row 8 -->
  <div class="board-row" style="top:611px"><span class="flap">M</span><span class="flap">A</span><span class="flap">L</span><span class="flap">A</span><span class="flap">Y</span><span class="flap">S</span><span class="flap">I</span><span class="flap">A</span><span class="flap">–</span><span class="flap flap--year">2</span><span class="flap flap--year">0</span><span class="flap flap--year">1</span><span class="flap flap--year">2</span></div>
  <svg class="flag" style="left:625px;top:614px" viewBox="0 0 30 18" aria-label="Malaysia flag"><rect width="30" height="18" fill="#fff"/><g fill="#cc0001"><rect y="0" width="30" height="1.3"/><rect y="2.6" width="30" height="1.3"/><rect y="5.1" width="30" height="1.3"/><rect y="7.7" width="30" height="1.3"/><rect y="10.3" width="30" height="1.3"/><rect y="12.9" width="30" height="1.3"/><rect y="15.4" width="30" height="1.3"/></g><rect width="15" height="10.3" fill="#010066"/><circle cx="6" cy="5.1" r="3" fill="#fc0"/><circle cx="7.2" cy="5.1" r="2.5" fill="#010066"/><circle cx="11" cy="5.1" r="1.6" fill="#fc0"/></svg>
  <figure class="snapshot" style="left:716px;top:580px;width:114px;height:90px;transform:rotate(2deg)"><div class="snapshot__fill" role="img" aria-label="Travel photo: traditional house in Malaysia" style="background:linear-gradient(180deg,#9fc3e0,#c9a25b 55%,#6b4a2c)"></div></figure>

  <!-- row 9 -->
  <div class="board-row" style="top:681px"><span class="flap">S</span><span class="flap">I</span><span class="flap">N</span><span class="flap">G</span><span class="flap">A</span><span class="flap">P</span><span class="flap">O</span><span class="flap">R</span><span class="flap">E</span><span class="flap flap--year">2</span><span class="flap flap--year">0</span><span class="flap flap--year">1</span><span class="flap flap--year">2</span></div>
  <svg class="flag" style="left:625px;top:684px" viewBox="0 0 30 18" aria-label="Singapore flag"><rect width="30" height="9" fill="#ef3340"/><rect y="9" width="30" height="9" fill="#fff"/><circle cx="6" cy="4.5" r="3" fill="#fff"/><circle cx="7.3" cy="4.5" r="2.7" fill="#ef3340"/></svg>

  <!-- row 10 -->
  <div class="board-row" style="top:751px"><span class="flap">V</span><span class="flap">I</span><span class="flap">E</span><span class="flap">T</span><span class="flap">N</span><span class="flap">A</span><span class="flap">M</span><span class="flap">,</span><span class="flap">L</span><span class="flap">A</span><span class="flap">O</span><span class="flap">S</span><span class="flap flap--amp">&amp;</span></div>
  <svg class="flag" style="left:625px;top:754px" viewBox="0 0 30 18" aria-label="Vietnam flag"><rect width="30" height="18" fill="#da251d"/><polygon points="15,3.5 16.4,7.6 20.7,7.6 17.2,10.1 18.5,14.2 15,11.7 11.5,14.2 12.8,10.1 9.3,7.6 13.6,7.6" fill="#ff0"/></svg>
  <svg class="flag" style="left:724px;top:754px" viewBox="0 0 30 18" aria-label="Laos flag"><rect width="30" height="18" fill="#ce1126"/><rect y="4.5" width="30" height="9" fill="#002868"/><circle cx="15" cy="9" r="3.6" fill="#fff"/></svg>

  <!-- row 11 -->
  <div class="board-row" style="top:821px"><span class="flap">C</span><span class="flap">A</span><span class="flap">M</span><span class="flap">B</span><span class="flap">O</span><span class="flap">D</span><span class="flap">I</span><span class="flap">A</span><span class="flap">–</span><span class="flap flap--year">2</span><span class="flap flap--year">0</span><span class="flap flap--year">1</span><span class="flap flap--year">3</span></div>
  <svg class="flag" style="left:625px;top:824px" viewBox="0 0 30 18" aria-label="Cambodia flag"><rect width="30" height="18" fill="#032ea1"/><rect y="4.5" width="30" height="9" fill="#e00025"/><rect x="11" y="6.5" width="8" height="5" fill="#fff"/></svg>
  <figure class="snapshot" style="left:716px;top:780px;width:114px;height:100px;transform:rotate(-2deg)"><div class="snapshot__fill" role="img" aria-label="Travel photo: two travellers in a field at sunset, Cambodia" style="background:linear-gradient(180deg,#a9b4c9,#c98f8a 50%,#6f6a4a)"></div></figure>

  <!-- row 12 -->
  <div class="board-row" style="top:891px"><span class="flap">E</span><span class="flap">U</span><span class="flap">R</span><span class="flap">O</span><span class="flap">P</span><span class="flap">E</span><span class="flap">–</span><span class="flap flap--year">2</span><span class="flap flap--year">0</span><span class="flap flap--year">1</span><span class="flap flap--year">5</span></div>
  <svg class="flag" style="left:535px;top:894px" viewBox="0 0 30 18" aria-label="European flag"><rect width="30" height="18" fill="#003399"/><g fill="#fc0"><circle cx="15" cy="4" r=".7"/><circle cx="17.5" cy="4.7" r=".7"/><circle cx="19.3" cy="6.5" r=".7"/><circle cx="20" cy="9" r=".7"/><circle cx="19.3" cy="11.5" r=".7"/><circle cx="17.5" cy="13.3" r=".7"/><circle cx="15" cy="14" r=".7"/><circle cx="12.5" cy="13.3" r=".7"/><circle cx="10.7" cy="11.5" r=".7"/><circle cx="10" cy="9" r=".7"/><circle cx="10.7" cy="6.5" r=".7"/><circle cx="12.5" cy="4.7" r=".7"/></g></svg>

  <blockquote class="quote">
    The world is a book and<br>
    those who do not travel read<br>
    <span class="quote__highlight">only one page.</span><svg class="quote__book" viewBox="0 0 66 34" aria-hidden="true"><g fill="none" stroke="#e9e9e9" stroke-width="2" stroke-linejoin="round"><path d="M33 8 Q20 2 6 5 L2 28 Q18 25 33 31 Q48 25 64 28 L60 5 Q46 2 33 8Z"/><path d="M33 8 L33 31"/><path d="M9 9 Q20 7 30 11 M9 14 Q20 12 30 16 M36 11 Q46 7 57 9 M36 16 Q46 12 57 14"/></g></svg>
    <cite class="quote__author">- Corwin of Veldmarsh</cite>
  </blockquote>

</main>
</body>
</html>
```